Business Card Design Project

Tarvolink - based in Melbourne, Australia. We plan, design, implement and support network infrastructure (Plemba, Hollvask, Kestavo, Stormpike etc).

Target Market(s)

Small/Medium enterprise and Corporate.

Industry/Entity Type

Business

```html
<!DOCTYPE html>
<html lang="en">
<head>
<meta charset="utf-8">
<title>Tarvolink Business Card</title>
<link href="https://fonts.googleapis.com/css2?family=Questrial&display=swap" rel="stylesheet">
<style>
  :root {
    --page: #e9e6e1;
    --card: #ffffff;
    --slate: #636466;
    --orange: #d9782a;
    --ink: #58595b;
    --light: #ffffff;
  }
  * { margin: 0; padding: 0; box-sizing: border-box; }
  html, body { width: 1200px; height: 858px; overflow: hidden; }
  body {
    background: var(--page);
    font-family: "Questrial", Arial, sans-serif;
    display: flex;
    align-items: center;
    justify-content: center;
    gap: 44px;
  }
  .card {
    position: relative;
    width: 530px;
    height: 303px;
    background: var(--card);
    box-shadow: 0 10px 24px rgba(0,0,0,0.18);
    overflow: hidden;
  }

  /* Front */
  .front .wordmark {
    position: absolute;
    left: 34px; top: 28px;
    font-size: 60px;
    letter-spacing: -1px;
    color: var(--slate);
    line-height: 1;
  }
  .front .person { position: absolute; left: 38px; top: 112px; }
  .person .name { font-size: 22px; color: var(--orange); line-height: 1.1; }
  .person .role { font-size: 12px; color: var(--ink); margin-top: 2px; }
  .front .contact {
    position: absolute; left: 38px; top: 170px;
    list-style: none;
    font-size: 12.5px; color: var(--ink); line-height: 1.45;
  }
  .front .rule {
    position: absolute; left: 0; right: 0; bottom: 40px;
    height: 2px; background: var(--orange);
  }
  .front .tagline-band {
    position: absolute; left: 0; right: 0; bottom: 0;
    height: 34px; background: var(--slate);
    color: var(--light); font-size: 13px;
    display: flex; align-items: center; padding-left: 38px;
  }

  /* Back */
  .back .band {
    position: absolute; left: 0; right: 0; top: 108px;
    height: 96px; background: var(--slate);
    display: flex; align-items: center; justify-content: center; gap: 16px;
  }
  .back .line {
    position: absolute; left: 0; right: 0; height: 2px; background: var(--orange);
  }
  .back .line.upper { top: 96px; }
  .back .line.lower { top: 214px; }
  .back .mark-dot {
    width: 54px; height: 54px; border-radius: 50%;
    border: 5px solid var(--light);
  }
  .back .wordmark { font-size: 54px; color: var(--light); letter-spacing: -1px; line-height: 1; }
  .partners {
    position: absolute; left: 30px; right: 30px; bottom: 34px;
    list-style: none;
    display: flex; justify-content: space-between; align-items: center;
    font-size: 14px; color: var(--ink);
  }
</style>
</head>
<body>
  <section class="card front" aria-label="Business card front">
    <div class="wordmark">Tarvolink</div>
    <div class="person">
      <div class="name">Employee Name</div>
      <div class="role">Managing Director</div>
    </div>
    <ul class="contact">
      <li>012 345 6789</li>
      <li>info@yourwebsite.com</li>
      <li>www.yourwebsite.com</li>
      <li>Address your Inc 00 2nd, Ave Larkfield, VX xxxxx</li>
    </ul>
    <div class="rule"></div>
    <div class="tagline-band">We plan, design, implement and support network infrastructure</div>
  </section>

  <section class="card back" aria-label="Business card back">
    <div class="line upper"></div>
    <div class="band">
      <div class="mark-dot"></div>
      <div class="wordmark">Tarvolink</div>
    </div>
    <div class="line lower"></div>
    <ul class="partners">
      <li>Plemba</li>
      <li>Hollvask</li>
      <li>Kestavo</li>
      <li>Stormpike</li>
    </ul>
  </section>
</body>
</html>
```